Business Card Design Project

looking for a stylish and simple double sided business card.
I am an artist - specialising in fashion illustration, portraits and murals.
the front should be simply my name and tag:

D U R E S K
Living in colour

My preference is for a Black background with DURESK in red or embossed.
Living in colour in White or multi-coloured.

the back will have detail:

Personalised Art
Portraits, Murals, Fashion Illustration

0437 582 190
duresk@duresk.com.au
www.duresk.com.au

Target Market(s)

Adults that are based in western speaking countries who have an appreciation for art and design. Portraits and wall art
Business owners who may need personalised all art for their business space. Murals and personalised canvass.
People in the fashion industry, who may require fashion illustrations.

Industry/Entity Type

Fashion

Requirements
Must have
• BOLD but simple at the same time, timeless modern element to it.
Nice to have
• simple lettering
Should not have
• Not too busy or wordy,

```html
<!DOCTYPE html>
<html lang="en">
<head>
<meta charset="utf-8">
<title>DURESK — Business Cards</title>
<link rel="stylesheet" href="https://fonts.googleapis.com/css2?family=Questrial&display=swap">
<style>
  :root {
    --stage-light: #f4f4f4;
    --stage-mid: #e2e2e2;
    --stage-dark: #b3b3b3;
    --card-red: #ff0000;
    --card-black: #000000;
    --ink-black: #000000;
    --ink-white: #ffffff;
    --ink-red: #ff0000;
    --ink-soft: #d9d9d9;
    --rule-on-red: rgba(255, 255, 255, 0.75);
    --rule-on-black: rgba(255, 255, 255, 0.35);
  }
  * { margin: 0; padding: 0; box-sizing: border-box; }
  html, body { width: 1200px; height: 720px; overflow: hidden; }
  body {
    font-family: "Questrial", "Century Gothic", sans-serif;
    background: radial-gradient(ellipse 60% 65% at 50% 45%, var(--stage-light) 0%, var(--stage-mid) 45%, var(--stage-dark) 100%);
    position: relative;
  }
  .card {
    position: absolute;
    width: 368px;
    height: 183px;
    text-align: center;
  }
  .card--red { background: var(--card-red); }
  .card--black { background: var(--card-black); }
  .card--front.card--red { left: 219px; top: 169px; }
  .card--back.card--red  { left: 613px; top: 169px; }
  .card--front.card--black { left: 219px; top: 369px; }
  .card--back.card--black  { left: 613px; top: 369px; }

  .line {
    position: absolute;
    left: 0; right: 0;
    white-space: nowrap;
    transform: translateY(-50%);
    line-height: 1;
  }
  .brand-name { top: 62px; font-size: 44px; letter-spacing: 1px; }
  .tagline { top: 119px; font-size: 17px; letter-spacing: 0.3px; }

  .rule {
    position: absolute;
    top: 94px;
    left: 40px;
    width: 283px;
    height: 0;
    border-top: 1px dashed;
  }
  .card--red .rule { border-color: var(--rule-on-red); }
  .card--black .rule { border-color: var(--rule-on-black); }

  .offer-title { top: 63px; font-size: 15px; }
  .offer-services { top: 82px; font-size: 16px; letter-spacing: 0.2px; }
  .contact { font-size: 12px; }
  .contact--phone { top: 122px; }
  .contact--email { top: 137px; }
  .contact--web { top: 152px; }

  .card--red .brand-name,
  .card--red .offer-title,
  .card--red .offer-services,
  .card--red .contact { color: var(--ink-black); }
  .card--red .tagline { color: var(--ink-white); }

  .card--black .brand-name,
  .card--black .offer-title,
  .card--black .offer-services { color: var(--ink-red); }
  .card--black .tagline { color: var(--ink-white); }
  .card--black .contact { color: var(--ink-soft); }
</style>
</head>
<body>
  <section class="card card--front card--red">
    <p class="line brand-name">DURESK</p>
    <p class="line tagline">Living in colour</p>
  </section>

  <section class="card card--back card--red">
    <p class="line offer-title">Personalised Art</p>
    <p class="line offer-services">portraits · murals · fashion illustration</p>
    <span class="rule"></span>
    <p class="line contact contact--phone">0437 582 190</p>
    <p class="line contact contact--email">duresk@duresk.com.au</p>
    <p class="line contact contact--web">www.duresk.com.au</p>
  </section>

  <section class="card card--front card--black">
    <p class="line brand-name">DURESK</p>
    <p class="line tagline">Living in colour</p>
  </section>

  <section class="card card--back card--black">
    <p class="line offer-title">Personalised Art</p>
    <p class="line offer-services">portraits · murals · fashion illustration</p>
    <span class="rule"></span>
    <p class="line contact contact--phone">0437 582 190</p>
    <p class="line contact contact--email">duresk@duresk.com.au</p>
    <p class="line contact contact--web">www.duresk.com.au</p>
  </section>
</body>
</html>
```